History Wall for Corporate Office

We are working on our corporate office wall to include a graphic with our history, and when we opened the schools and dance studios.
We are looking for a professional look, vibrant graphic, but clean and very clear to understand.
The wall is going up from floor 1 to floor 2. Please see photos attached as reference.
Measurements provided as well.
Do not include the master logo as part of this design, as the master logo it's placed in the wall right next to this one (photo as reference will show this).
Things to consider:
- We want to include photos of the schools/studio openings. Attached are the photos of each school opening.
- Follow brand guidelines
- Mainly using Master Color palette (blues and yellows) with touches of the other colors if needed
Here's the order of school/studio openings:
1968 Bright Path Hollowmere
1971 Bright Path Fernwick
1975 Bright Path Harlow
1976 The Bright Path Conservatory of Dance
1978 Bright Path Collegiate
1979 Bright Path Cobalt • Preschool & Elementary School
1980 Bright Path Las Brisas
1981 Bright Path Cedar Crest
1984 Bright Path Middle School
1989 Bright Path Dorsey
1990 Bright Path Whitford
2005 Bright Path Garnet
2008 Bright Path Schools 40th Anniversary
2015 NHMS Talbot Studio
2016 NHMS Aspen Hollow Studio
2017 NHMS Cedar Crest Studio
2018 Bright Path Schools 50th Anniversary
2021 Kinetic Leagues Coastline
2022 NHMS Cedar Crest Studio
2024 Bright Path Sutter Ridge
Fonts to be used: Fellix (main font) and Handsome (highlights-if needed)
Sending two graphic ideas as reference of the design direction we would like to have.

```html
<!DOCTYPE html>
<html lang="en">
<head>
<meta charset="utf-8">
<title>Bright Path Schools / Studio Openings Timeline</title>
<link rel="stylesheet" href="https://fonts.googleapis.com/css2?family=Outfit:wght@600&family=Montserrat:wght@500;600;700&family=Kalam:wght@700&family=Oswald:wght@300&display=swap">
<style>
  :root {
    --brand-blue: #0d5aa7;
    --box-blue: #0a64a8;
    --sky-blue: #7fa6d6;
    --accent-orange: #f7821f;
    --node-orange: #f26b21;
    --accent-green: #17704a;
    --connector: #8c8c8c;
    --ink: #111111;
    --wall-edge: #000000;
    --note-red: #ff1a1a;
    --note-line: #c8c83a;
    --paper: #ffffff;
  }
  html, body {
    margin: 0;
    padding: 0;
    width: 1200px;
    height: 1078px;
    overflow: hidden;
    background: var(--paper);
  }
  .wall { display: block; width: 1200px; height: 1078px; }
  .wall-edge { fill: var(--wall-edge); }
  .heading-box { fill: var(--brand-blue); }
  .heading-text { font-family: "Montserrat", sans-serif; font-weight: 500; font-size: 19px; fill: #fff; text-anchor: middle; }
  .heading-accent { font-family: "Kalam", cursive; font-weight: 700; font-size: 24px; fill: #0d82c4; text-anchor: middle; letter-spacing: 0.5px; }
  .band { fill: none; stroke: url(#bandGradient); stroke-width: 24; stroke-linejoin: round; stroke-linecap: round; }
  .band-cap { fill: none; stroke: #4a9ad8; stroke-width: 24; stroke-linecap: round; }
  .band-dash { fill: none; stroke: #fff; stroke-width: 1; stroke-dasharray: 3 3; opacity: .9; }
  .node { fill: none; stroke: var(--node-orange); stroke-width: 1.6; }
  .flow { stroke-width: 4; stroke-linecap: round; }
  .connector { stroke: var(--connector); stroke-width: 3.5; }
  .connector-cap { fill: var(--connector); }
  .year { font-family: "Outfit", sans-serif; font-weight: 600; font-size: 41px; letter-spacing: -1.5px; }
  .year--blue { fill: var(--brand-blue); }
  .year--sky { fill: var(--sky-blue); }
  .year--orange { fill: var(--accent-orange); }
  .year--green { fill: var(--accent-green); }
  .title { font-family: "Montserrat", sans-serif; font-weight: 700; font-size: 16px; fill: var(--ink); }
  .title--compact { font-size: 13px; }
  .title--medium { font-size: 14px; }
  .blurb { font-family: "Montserrat", sans-serif; font-weight: 600; font-size: 6.8px; fill: var(--ink); }
  .blurb--spaced { letter-spacing: 1px; font-size: 5.6px; font-weight: 700; }
  .photo { fill: url(#photoGradient); }
  .photo--interior { fill: url(#interiorGradient); }
  .placeholder { fill: var(--box-blue); }
  .note-label { font-family: "Oswald", sans-serif; font-weight: 300; font-size: 17px; fill: var(--note-red); letter-spacing: 3px; }
  .note-text { font-family: "Montserrat", sans-serif; font-weight: 700; font-size: 16px; fill: var(--note-red); }
  .note-arrow { stroke: var(--note-red); stroke-width: 2.5; }
  .note-head { fill: var(--note-red); }
  .note-leader { stroke: var(--note-line); stroke-width: 0.8; fill: none; }
</style>
</head>
<body>
<svg class="wall" viewBox="0 0 1200 1078" xmlns="http://www.w3.org/2000/svg">
  <defs>
    <linearGradient id="bandGradient" gradientUnits="userSpaceOnUse" x1="53" y1="0" x2="1150" y2="0">
      <stop offset="0" stop-color="#233f9a"/>
      <stop offset=".45" stop-color="#1f6fbf"/>
      <stop offset="1" stop-color="#2f86cf"/>
    </linearGradient>
    <linearGradient id="photoGradient" x1="0" y1="0" x2="0" y2="1">
      <stop offset="0" stop-color="#c9d3dc"/>
      <stop offset=".5" stop-color="#7d8f6e"/>
      <stop offset="1" stop-color="#5e7a3a"/>
    </linearGradient>
    <linearGradient id="interiorGradient" x1="0" y1="0" x2="0" y2="1">
      <stop offset="0" stop-color="#d7dde3"/>
      <stop offset=".55" stop-color="#4a5560"/>
      <stop offset="1" stop-color="#2a2f36"/>
    </linearGradient>
    <marker id="headBlue" viewBox="0 0 10 10" refX="5" refY="5" markerWidth="3" markerHeight="3" orient="auto"><path d="M0 0L10 5L0 10z" fill="#2a8fd6"/></marker>
    <marker id="headGreen" viewBox="0 0 10 10" refX="5" refY="5" markerWidth="3" markerHeight="3" orient="auto"><path d="M0 0L10 5L0 10z" fill="#3bb54a"/></marker>
    <marker id="headYellow" viewBox="0 0 10 10" refX="5" refY="5" markerWidth="3" markerHeight="3" orient="auto"><path d="M0 0L10 5L0 10z" fill="#f5b324"/></marker>
    <marker id="headOrange" viewBox="0 0 10 10" refX="5" refY="5" markerWidth="3" markerHeight="3" orient="auto"><path d="M0 0L10 5L0 10z" fill="#f26b21"/></marker>
    <marker id="headLight" viewBox="0 0 10 10" refX="5" refY="5" markerWidth="3" markerHeight="3" orient="auto"><path d="M0 0L10 5L0 10z" fill="#6fa8dc"/></marker>
    <marker id="headIndigo" viewBox="0 0 10 10" refX="5" refY="5" markerWidth="3" markerHeight="3" orient="auto"><path d="M0 0L10 5L0 10z" fill="#4a6fd8"/></marker>
  </defs>

  <!-- wall outline -->
  <polygon class="wall-edge" points="0,0 1200,0 1200,89 1126,89 1126,0 0,177"/>
  <polygon class="wall-edge" points="325,1078 325,1032 431,1032 431,986 526,986 526,946 631,946 631,899 739,899 739,852 837,852 837,809 945,809 945,763 1067,763 1067,708 1200,708 1200,1078"/>

  <!-- heading -->
  <g class="heading">
    <rect class="heading-box" x="57" y="197" width="208" height="67" rx="11"/>
    <text class="heading-text" x="161" y="217">BRIGHT PATH</text>
    <text class="heading-text" x="161" y="238">SCHOOLS/STUDIO</text>
    <text class="heading-text" x="161" y="259">OPENINGS</text>
    <text class="heading-accent" x="161" y="296">TIMELINE</text>
  </g>

  <!-- connectors -->
  <g class="connectors">
    <line class="connector" x1="55" y1="711" x2="55" y2="570"/><rect class="connector-cap" x="50" y="568" width="10" height="3"/>
    <line class="connector" x1="116" y1="687" x2="116" y2="837"/><rect class="connector-cap" x="111" y="836" width="10" height="3"/>
    <line class="connector" x1="166" y1="639" x2="166" y2="497"/><rect class="connector-cap" x="161" y="495" width="10" height="3"/>
    <line class="connector" x1="224" y1="639" x2="224" y2="782"/><rect class="connector-cap" x="219" y="781" width="10" height="3"/>
    <line class="connector" x1="273" y1="613" x2="273" y2="466"/><rect class="connector-cap" x="268" y="464" width="10" height="3"/>
    <line class="connector" x1="318" y1="527" x2="318" y2="686"/><rect class="connector-cap" x="313" y="685" width="10" height="3"/>
    <line class="connector" x1="360" y1="480" x2="360" y2="391"/><rect class="connector-cap" x="355" y="389" width="10" height="3"/>
    <line class="connector" x1="427" y1="458" x2="427" y2="601"/><rect class="connector-cap" x="422" y="600" width="10" height="3"/>
    <line class="connector" x1="484" y1="472" x2="484" y2="343"/><rect class="connector-cap" x="479" y="341" width="10" height="3"/>
    <line class="connector" x1="536" y1="497" x2="536" y2="639"/><rect class="connector-cap" x="531" y="638" width="10" height="3"/>
    <line class="connector" x1="601" y1="488" x2="601" y2="378"/><rect class="connector-cap" x="596" y="376" width="10" height="3"/>
    <line class="connector" x1="654" y1="447" x2="654" y2="591"/><rect class="connector-cap" x="649" y="590" width="10" height="3"/>
    <line class="connector" x1="703" y1="381" x2="703" y2="292"/><rect class="connector-cap" x="698" y="290" width="10" height="3"/>
    <line class="connector" x1="758" y1="351" x2="758" y2="495"/><rect class="connector-cap" x="753" y="494" width="10" height="3"/>
    <line class="connector" x1="813" y1="353" x2="813" y2="317"/><rect class="connector-cap" x="808" y="315" width="10" height="3"/>
    <line class="connector" x1="875" y1="385" x2="875" y2="462"/><rect class="connector-cap" x="870" y="461" width="10" height="3"/>
    <line class="connector" x1="943" y1="394" x2="943" y2="274"/><rect class="connector-cap" x="938" y="272" width="10" height="3"/>
    <line class="connector" x1="1007" y1="382" x2="1007" y2="492"/><rect class="connector-cap" x="1002" y="491" width="10" height="3"/>
    <line class="connector" x1="1058" y1="348" x2="1058" y2="301"/><rect class="connector-cap" x="1053" y="299" width="10" height="3"/>
    <line class="connector" x1="1117" y1="319" x2="1117" y2="422"/><rect class="connector-cap" x="1112" y="421" width="10" height="3"/>
  </g>

  <!-- timeline band -->
  <g class="timeline-band">
    <line class="band-cap" x1="1117" y1="319" x2="1150" y2="319"/>
    <polyline class="band" points="53,711 116,687 166,639 224,639 273,613 318,527 360,480 427,458 484,472 536,497 601,488 654,447 703,381 758,351 813,353 875,385 943,394 1007,382 1058,348 1117,319"/>
    <polyline class="band-dash" points="53,711 116,687 166,639 224,639 273,613 318,527 360,480 427,458 484,472 536,497 601,488 654,447 703,381 758,351 813,353 875,385 943,394 1007,382 1058,348 1117,319 1150,319"/>
    <g class="flow-arrows">
      <line class="flow" stroke="#2a8fd6" marker-end="url(#headBlue)" x1="66" y1="706" x2="100" y2="693"/>
      <line class="flow" stroke="#3bb54a" marker-end="url(#headGreen)" x1="126" y1="677" x2="153" y2="651"/>
      <line class="flow" stroke="#f5b324" marker-end="url(#headYellow)" x1="178" y1="639" x2="209" y2="639"/>
      <line class="flow" stroke="#f26b21" marker-end="url(#headOrange)" x1="234" y1="634" x2="260" y2="620"/>
      <line class="flow" stroke="#6fa8dc" marker-end="url(#headLight)" x1="282" y1="596" x2="307" y2="547"/>
      <line class="flow" stroke="#4a6fd8" marker-end="url(#headIndigo)" x1="326" y1="518" x2="350" y2="491"/>
      <line class="flow" stroke="#3bb54a" marker-end="url(#headGreen)" x1="373" y1="476" x2="411" y2="463"/>
      <line class="flow" stroke="#f5b324" marker-end="url(#headYellow)" x1="438" y1="461" x2="470" y2="468"/>
      <line class="flow" stroke="#f26b21" marker-end="url(#headOrange)" x1="494" y1="477" x2="523" y2="490"/>
      <line class="flow" stroke="#6fa8dc" marker-end="url(#headLight)" x1="549" y1="495" x2="585" y2="490"/>
      <line class="flow" stroke="#4a6fd8" marker-end="url(#headIndigo)" x1="612" y1="480" x2="640" y2="457"/>
      <line class="flow" stroke="#3bb54a" marker-end="url(#headGreen)" x1="664" y1="434" x2="691" y2="397"/>
      <line class="flow" stroke="#f26b21" marker-end="url(#headOrange)" x1="714" y1="375" x2="744" y2="359"/>
      <line class="flow" stroke="#f5b324" marker-end="url(#headYellow)" x1="769" y1="351" x2="799" y2="353"/>
      <line class="flow" stroke="#3bb54a" marker-end="url(#headGreen)" x1="825" y1="359" x2="860" y2="377"/>
      <line class="flow" stroke="#6fa8dc" marker-end="url(#headLight)" x1="889" y1="387" x2="926" y2="392"/>
      <line class="flow" stroke="#4a6fd8" marker-end="url(#headIndigo)" x1="956" y1="392" x2="991" y2="385"/>
      <line class="flow" stroke="#3bb54a" marker-end="url(#headGreen)" x1="1017" y1="375" x2="1045" y2="357"/>
      <line class="flow" stroke="#4a6fd8" marker-end="url(#headIndigo)" x1="1070" y1="342" x2="1102" y2="326"/>
    </g>
    <g class="nodes">
      <ellipse class="node" cx="53" cy="711" rx="11" ry="6"/>
      <ellipse class="node" cx="116" cy="687" rx="11" ry="6"/>
      <ellipse class="node" cx="166" cy="639" rx="11" ry="6"/>
      <ellipse class="node" cx="224" cy="639" rx="11" ry="6"/>
      <ellipse class="node" cx="273" cy="613" rx="11" ry="6"/>
      <ellipse class="node" cx="318" cy="527" rx="11" ry="6"/>
      <ellipse class="node" cx="360" cy="480" rx="11" ry="6"/>
      <ellipse class="node" cx="427" cy="458" rx="11" ry="6"/>
      <ellipse class="node" cx="484" cy="472" rx="11" ry="6"/>
      <ellipse class="node" cx="536" cy="497" rx="11" ry="6"/>
      <ellipse class="node" cx="601" cy="488" rx="11" ry="6"/>
      <ellipse class="node" cx="654" cy="447" rx="11" ry="6"/>
      <ellipse class="node" cx="703" cy="381" rx="11" ry="6"/>
      <ellipse class="node" cx="758" cy="351" rx="11" ry="6"/>
      <ellipse class="node" cx="813" cy="353" rx="11" ry="6"/>
      <ellipse class="node" cx="875" cy="385" rx="11" ry="6"/>
      <ellipse class="node" cx="943" cy="394" rx="11" ry="6"/>
      <ellipse class="node" cx="1007" cy="382" rx="11" ry="6"/>
      <ellipse class="node" cx="1058" cy="348" rx="11" ry="6"/>
      <ellipse class="node" cx="1117" cy="319" rx="11" ry="6"/>
    </g>
  </g>

  <!-- milestones -->
  <g class="milestone">
    <text class="year year--blue" x="34" y="565">1968</text>
    <text class="title" transform="translate(52 531) rotate(-90)">Hollowmere</text>
    <text class="blurb" transform="translate(61 531) rotate(-90)">Lorem ipsum dolor sit amet,</text>
    <rect class="photo" role="img" aria-label="Photo of the Bright Path Hollowmere campus opening" x="64" y="431" width="50" height="101" rx="8"/>
  </g>
  <g class="milestone">
    <text class="year year--blue" x="94" y="871">1971</text>
    <text class="title" transform="translate(113 965) rotate(-90)">Fernwick</text>
    <text class="blurb" transform="translate(121 977) rotate(-90)">Lorem ipsum dolor sit amet,</text>
    <rect class="photo" role="img" aria-label="Photo of the Bright Path Fernwick campus opening" x="123" y="876" width="51" height="101" rx="8"/>
  </g>
  <g class="milestone">
    <text class="year year--blue" x="144" y="492">1975</text>
    <text class="title" transform="translate(161 459) rotate(-90)">Harlow</text>
    <text class="blurb" transform="translate(170 459) rotate(-90)">Lorem ipsum dolor sit amet,</text>
    <rect class="photo" role="img" aria-label="Photo of the Bright Path Harlow house-style campus" x="174" y="358" width="49" height="102" rx="8"/>
  </g>
  <g class="milestone">
    <text class="year year--blue" x="203" y="816">1976</text>
    <text class="title title--compact" transform="translate(220 991) rotate(-90)">Conservatory of Dance</text>
    <text class="blurb" transform="translate(229 991) rotate(-90)">Lorem ipsum dolor sit amet,</text>
    <rect class="placeholder" x="233" y="820" width="50" height="101" rx="9"/>
  </g>
  <g class="milestone">
    <text class="year year--blue" x="252" y="461">1978</text>
    <text class="title" transform="translate(270 428) rotate(-90)">Collegiate</text>
    <text class="blurb" transform="translate(279 428) rotate(-90)">Lorem ipsum dolor sit amet,</text>
    <rect class="placeholder" x="283" y="328" width="49" height="100" rx="9"/>
  </g>
  <g class="milestone">
    <text class="year year--blue" x="296" y="720">1979</text>
    <text class="title" transform="translate(316 782) rotate(-90)">Cobalt</text>
    <text class="blurb blurb--spaced" transform="translate(323 824) rotate(-90)">Preschool &amp; Elementary</text>
    <rect class="photo" role="img" aria-label="Two photos of the Bright Path Cobalt preschool and elementary buildings" x="328" y="723" width="49" height="101" rx="8"/>
  </g>
  <g class="milestone">
    <text class="year year--sky" x="340" y="385">1980</text>
    <text class="title" transform="translate(358 354) rotate(-90)">Las Brisas</text>
    <text class="blurb" transform="translate(366 354) rotate(-90)">Lorem ipsum dolor sit amet,</text>
    <rect class="photo" role="img" aria-label="Photo of a tall tree beside the Bright Path Las Brisas sign" x="369" y="253" width="52" height="101" rx="8"/>
  </g>
  <g class="milestone">
    <text class="year year--sky" x="406" y="637">1981</text>
    <text class="title" transform="translate(425 773) rotate(-90)">Cedar Crest</text>
    <text class="blurb" transform="translate(433 743) rotate(-90)">Lorem ipsum dolor sit amet,</text>
    <rect class="photo" role="img" aria-label="Photo of the Bright Path Cedar Crest sign and lawn" x="436" y="641" width="50" height="101" rx="8"/>
  </g>
  <g class="milestone">
    <text class="year year--orange" x="463" y="338">1984</text>
    <text class="title" transform="translate(483 304) rotate(-90)">Middle School</text>
    <text class="blurb" transform="translate(490 304) rotate(-90)">Lorem ipsum dolor sit amet,</text>
    <rect class="photo" role="img" aria-label="Photo of the Bright Path Middle School entrance" x="493" y="204" width="50" height="101" rx="8"/>
  </g>
  <g class="milestone">
    <text class="year year--orange" x="516" y="671">1989</text>
    <text class="title" transform="translate(535 746) rotate(-90)">Dorsey</text>
    <text class="blurb" transform="translate(542 779) rotate(-90)">Lorem ipsum dolor sit amet,</text>
    <rect class="photo" role="img" aria-label="Photo of the Bright Path Dorsey building across a parking lot" x="545" y="679" width="51" height="100" rx="8"/>
  </g>
  <g class="milestone">
    <text class="year year--green" x="581" y="372">1990</text>
    <text class="title" transform="translate(600 341) rotate(-90)">Whitford</text>
    <text class="blurb" transform="translate(607 341) rotate(-90)">Lorem ipsum dolor sit amet,</text>
    <rect class="photo" role="img" aria-label="Photo of the Bright Path Whitford signage" x="612" y="239" width="50" height="102" rx="8"/>
  </g>
  <g class="milestone">
    <text class="year year--green" x="633" y="624">2005</text>
    <text class="title" transform="translate(652 731) rotate(-90)">Garnet</text>
    <text class="blurb" transform="translate(659 731) rotate(-90)">Lorem ipsum dolor sit amet,</text>
    <rect class="photo" role="img" aria-label="Photo of pine trees behind the Bright Path Garnet sign" x="663" y="629" width="50" height="101" rx="8"/>
  </g>
  <g class="milestone">
    <text class="year year--blue" x="681" y="286">2008</text>
    <text class="title" transform="translate(702 253) rotate(-90)">40th Anniversary</text>
    <text class="blurb" transform="translate(709 253) rotate(-90)">Lorem ipsum dolor sit amet,</text>
    <rect class="placeholder" x="711" y="152" width="50" height="101" rx="9"/>
  </g>
  <g class="milestone">
    <text class="year year--blue" x="738" y="529">2015</text>
    <text class="title" transform="translate(757 667) rotate(-90)">Talbot Studio</text>
    <text class="blurb" transform="translate(764 634) rotate(-90)">Lorem ipsum dolor sit amet,</text>
    <rect class="photo photo--interior" role="img" aria-label="Photo of the NHMS Talbot Studio storefront" x="767" y="532" width="51" height="102" rx="8"/>
  </g>
  <g class="milestone">
    <text class="year year--blue" x="792" y="311">2016</text>
    <text class="title" transform="translate(811 279) rotate(-90)">Aspen Hollow Studio</text>
    <text class="blurb" transform="translate(818 279) rotate(-90)">Lorem ipsum dolor sit amet,</text>
    <rect class="photo" role="img" aria-label="Photo of the NHMS Aspen Hollow Studio street front" x="822" y="178" width="50" height="101" rx="8"/>
  </g>
  <g class="milestone">
    <text class="year year--blue" x="853" y="498">2017</text>
    <text class="title" transform="translate(874 698) rotate(-90)">Cedar Crest Studio</text>
    <text class="blurb" transform="translate(881 601) rotate(-90)">Lorem ipsum dolor sit amet,</text>
    <rect class="photo photo--interior" role="img" aria-label="Photos of the NHMS Cedar Crest Studio interior and front desk" x="884" y="501" width="51" height="100" rx="8"/>
  </g>
  <g class="milestone">
    <text class="year year--blue" x="921" y="270">2018</text>
    <text class="title" transform="translate(942 237) rotate(-90)">50th Anniversary</text>
    <text class="blurb" transform="translate(949 237) rotate(-90)">Lorem ipsum dolor sit amet,</text>
    <rect class="placeholder" x="952" y="136" width="51" height="101" rx="9"/>
  </g>
  <g class="milestone">
    <text class="year year--blue" x="985" y="524">2021</text>
    <text class="title title--medium" transform="translate(1006 674) rotate(-90)">Leagues Coastline</text>
    <text class="blurb" transform="translate(1013 630) rotate(-90)">Lorem ipsum dolor sit amet,</text>
    <rect class="placeholder" x="1016" y="529" width="51" height="101" rx="9"/>
  </g>
  <g class="milestone">
    <text class="year year--sky" x="1036" y="293">2022</text>
    <text class="title" transform="translate(1056 261) rotate(-90)">Cedar Crest Studio</text>
    <text class="blurb" transform="translate(1064 261) rotate(-90)">Lorem ipsum dolor sit amet,</text>
    <rect class="photo photo--interior" role="img" aria-label="Photo of the NHMS Cedar Crest Studio building front" x="1067" y="161" width="50" height="101" rx="8"/>
  </g>
  <g class="milestone">
    <text class="year year--sky" x="1095" y="453">2024</text>
    <text class="title title--medium" transform="translate(1115 561) rotate(-90)">Sutter Ridge</text>
    <text class="blurb" transform="translate(1123 561) rotate(-90)">Lorem ipsum dolor sit amet,</text>
    <rect class="photo" role="img" aria-label="Photo of the Bright Path Sutter Ridge sign and landscaping" x="1125" y="459" width="50" height="101" rx="8"/>
  </g>

  <!-- measurement notes -->
  <g class="measure-notes">
    <line class="note-arrow" x1="632" y1="923" x2="728" y2="923"/>
    <path class="note-head" d="M739 923L726 916L726 930z"/>
    <text class="note-label" x="637" y="952">A STEP DEPTH</text>
    <line class="note-arrow" x1="446" y1="987" x2="446" y2="1020"/>
    <path class="note-head" d="M446 1032L438 1018L454 1018z"/>
    <text class="note-label" x="467" y="1024">A STEP HEIGHT</text>
    <path class="note-leader" d="M667 963L616 1022"/>
    <path class="note-leader" d="M580 1018L607 1025"/>
    <text class="note-text" x="612" y="1040">I need to know</text>
    <text class="note-text" x="612" y="1061">To properly resize the artwork</text>
  </g>
</svg>
</body>
</html>
```